Electric Vehicle (EV) Charging Station Program

My company is working with a group who is looking for sites to install EV chargers. The flyer/brochure will be distributed to potential clients with a location for an EV charger (e.g. businesses where employees park their cars and could use the chargers during the day, etc.). The group that is looking for sites will pay for everything pertaining to the chargers, they are mainly looking for sites and locations. We are in need of a one page flyer that has a clean looking design and promotes EV chargers and vehicles. Likely a green/blue theme and ideally a background set in a city/town street with an EV car and charger. We also would like some trees in the picture and possibly the sun. We have attached a sample of our initial idea for a type of look or feel, looking for something more professional, and moving away from the dessert setting and to an urban one instead. We'd like to have two logos near the top (attached), have the information from the text box image somewhere in the design (attached), incorporate two pictures of potential chargers (attached but please feel free to use different photos for these. We will likely be installing Voltmora and KDT brand chargers), and have the contact information for our representative likely on the bottom (attached). We would like the design format to allow us to change text later if we want to change the wording. This theme may be used for other brochures in the future so we have a “company look”. Again, the attached one was a rough initial mark up, please feel free to take it where you'd like just with the items listed incorporated (green trees, sun, water maybe).

```html
<!DOCTYPE html>
<html lang="en">
<head>
<meta charset="utf-8">
<title>VRS / Lumen Grid Partners – Free EV Charging Station Program</title>
<link rel="stylesheet" href="https://fonts.googleapis.com/css2?family=Montserrat:wght@500;600;700;800&display=swap">
<style>
  :root {
    --green: #0c7440;
    --gold: #f3a81e;
    --paper: #f8f8fa;
    --white: #ffffff;
    --frame: #2c2c2c;
    --sky-top: #5f97d2;
    --sky-low: #cfe2f2;
    --city: #a9b4bf;
    --trees: #4f8a3e;
    --street: #6d747b;
    --navy: #1e3a6e;
    --lumen: #2a76b8;
  }
  * { margin: 0; padding: 0; box-sizing: border-box; }
  html, body {
    width: 933px; height: 1200px; overflow: hidden;
    background: var(--white);
    font-family: "Montserrat", Arial, sans-serif;
  }
  .canvas { position: relative; width: 933px; height: 1200px; }
  .flyer {
    position: absolute; left: 22px; top: 28px; width: 890px; height: 1145px;
    border: 1.5px solid var(--frame);
    box-shadow: 3px 3px 5px rgba(0,0,0,.35);
    overflow: hidden;
    background: var(--green);
  }
  .street-photo {
    position: absolute; left: 0; top: 0; width: 100%; height: 580px;
    background:
      radial-gradient(circle at 82% 14%, rgba(255,244,200,.9) 0, rgba(255,236,170,.35) 70px, rgba(255,236,170,0) 150px),
      linear-gradient(180deg, var(--sky-top) 0%, var(--sky-low) 30%, var(--city) 42%, var(--trees) 58%, #5d8f4a 68%, var(--street) 82%, #5c6268 100%);
  }
  .shapes { position: absolute; left: 0; top: 0; width: 100%; height: 100%; }
  .logo-box {
    position: absolute; top: 27px; height: 74px; background: var(--white);
    display: flex; align-items: center; justify-content: center; gap: 8px;
    font-weight: 700;
  }
  .logo-primary { left: 48px; width: 165px; color: var(--navy); font-size: 34px; }
  .logo-partner { left: 698px; width: 142px; color: var(--lumen); font-size: 19px; }
  .logo-dot { width: 12px; height: 12px; border-radius: 50%; background: currentColor; }
  .charger { position: absolute; border-radius: 6px; }
  .charger-voltmora {
    left: 59px; top: 239px; width: 174px; height: 320px;
    background: linear-gradient(90deg, #b8b8b8 0%, #e8792a 18%, #f08a35 60%, #c9c9c9 100%);
  }
  .charger-kdt {
    left: 261px; top: 224px; width: 128px; height: 345px;
    background: linear-gradient(90deg, #f2f2f2 0%, #e4e4e4 70%, #bdbdbd 100%);
  }
  .headline {
    position: absolute; left: 42px; top: 604px;
    color: var(--white); font-weight: 800; font-size: 49px; letter-spacing: .2px;
    white-space: nowrap;
  }
  .subhead {
    position: absolute; left: 43px; top: 664px;
    color: var(--gold); font-weight: 700; font-size: 30px; white-space: nowrap;
  }
  .services-title {
    position: absolute; left: 43px; top: 746px;
    color: var(--gold); font-weight: 700; font-size: 32px; letter-spacing: 4px;
  }
  .services-list { position: absolute; left: 44px; top: 802px; list-style: none; }
  .services-list li {
    display: flex; align-items: center; height: 40.5px;
    color: var(--white); font-weight: 500; font-size: 24px; letter-spacing: .3px;
    white-space: nowrap;
  }
  .tick { width: 28px; height: 22px; margin-right: 33px; flex: none; }
  .contact {
    position: absolute; right: 34px; top: 980px; text-align: right; color: var(--green);
  }
  .contact-cta { font-weight: 800; font-size: 17.2px; letter-spacing: 1.3px; line-height: 26px; }
  .contact-line { font-weight: 600; font-size: 23.5px; line-height: 35.5px; }
</style>
</head>
<body>
<div class="canvas">
  <div class="flyer">
    <div class="street-photo" role="img" aria-label="Photo of a sunny city street with an electric car parked at a charger, green trees along the sidewalk and the sun in a blue sky"></div>

    <svg class="shapes" viewBox="35 45 1430 1840" preserveAspectRatio="none" aria-hidden="true">
      <path d="M35,560 C120,700 250,790 420,800 C600,810 700,770 850,790 C1050,815 1200,900 1330,905 C1400,905 1440,885 1465,865 L1465,1885 L35,1885 Z" fill="var(--green)"/>
      <path d="M35,560 C120,700 250,790 420,800 C600,810 700,770 850,790 C1050,815 1200,900 1330,905 C1400,905 1440,885 1465,865" fill="none" stroke="var(--gold)" stroke-width="6"/>
      <path d="M630,1885 C720,1660 960,1520 1260,1512 C1360,1510 1430,1518 1465,1525 L1465,1885 Z" fill="var(--paper)"/>
    </svg>

    <div class="logo-box logo-primary"><span class="logo-dot"></span>VRS</div>
    <div class="logo-box logo-partner">Lumen Grid<span class="logo-dot"></span></div>

    <div class="charger charger-voltmora" role="img" aria-label="Photo of an orange Voltmora DC fast charging station"></div>
    <div class="charger charger-kdt" role="img" aria-label="Photo of a white KDT DC fast charging station"></div>

    <h1 class="headline">VRS/Lumen Grid Partners (LGP)</h1>
    <p class="subhead">Free Electric Vehicle Charging Station Program</p>

    <h2 class="services-title">Our Services</h2>
    <ul class="services-list">
      <li><svg class="tick" viewBox="0 0 28 22"><path d="M2,12 L10,20 L26,2" fill="none" stroke="var(--gold)" stroke-width="2.5"/></svg>No Cost to Customer</li>
      <li><svg class="tick" viewBox="0 0 28 22"><path d="M2,12 L10,20 L26,2" fill="none" stroke="var(--gold)" stroke-width="2.5"/></svg>Customer Receives Monthly Rental Income</li>
      <li><svg class="tick" viewBox="0 0 28 22"><path d="M2,12 L10,20 L26,2" fill="none" stroke="var(--gold)" stroke-width="2.5"/></svg>Customer Receives Profit Sharing</li>
      <li><svg class="tick" viewBox="0 0 28 22"><path d="M2,12 L10,20 L26,2" fill="none" stroke="var(--gold)" stroke-width="2.5"/></svg>Help Meet Sustainability Plan Goals</li>
    </ul>

    <div class="contact">
      <p class="contact-cta">SET UP AN APPOINTMENT TODAY</p>
      <p class="contact-line">Mara Ellison</p>
      <p class="contact-line">mellison@VRSpower.com</p>
      <p class="contact-line">(555) 014-2286</p>
    </div>
  </div>
</div>
</body>
</html>
```